Brim Vantage Partners Consulting Company Template

Microsoft Word template for a professional retail consulting company that can suggestingly mimic the attached design, but in vertical fashion - . Important - It doesn't have to mimic this design. I accept creativity, professionalism, and eye catching work!

I'd also like suggestingly the globe of the attached logo to appear as an imprint in the background

To win the contest, please make it look extremely impressive, attention grabbing, and don't fear giving it your own creative unique design elements.

The Word template is needed for me to create Word documents from, so it is highly important that I would be able to write memos in Word, and for those same memos to look clean.

Target Market(s)

Retailers interested in consulting services from Tolven Supply

Font styles to use
Serif

Requirements
Must have
• Brim Vantage Partners logo represented. Also, red and black logo colors. A professional, modern, outstanding look and design. Must be somewhat bold and upmarket.
Nice to have
• I accept all forms of creativity.
Should not have
• Cartoon / child looking

```html
<!DOCTYPE html>
<html lang="en">
<head>
<meta charset="utf-8">
<title>Brim Vantage Partners – Document Template</title>
<link href="https://fonts.googleapis.com/css2?family=Fira+Sans:wght@400;500;600;700&family=Oswald:wght@500&family=Noto+Serif:wght@400&display=swap" rel="stylesheet">
<style>
:root{
  --red:#e8132b;
  --red-soft:#f7c9cf;
  --maroon:#5a1420;
  --ink:#2b2b2b;
  --backdrop:#d9e2e1;
  --paper:#ffffff;
  --photo-green:#5d7a3c;
  --photo-pink:#f1b9bd;
}
*{margin:0;padding:0;box-sizing:border-box}
html,body{width:1200px;height:1200px;overflow:hidden}
body{background:var(--backdrop);position:relative;font-family:"Fira Sans",sans-serif;color:var(--ink)}
.page{position:absolute;background:var(--paper);box-shadow:4px 5px 6px rgba(0,0,0,.45);overflow:hidden}
.band{position:absolute;left:0;right:0;background:var(--red);color:#fff;display:flex;align-items:center;justify-content:center}

/* cover */
.cover{left:87px;top:155px;width:588px;height:820px}
.cover-photo{position:absolute;left:32px;top:29px;width:522px;height:594px;
  background:linear-gradient(115deg,var(--photo-green) 0%,#7f9a52 35%,#caa2a4 62%,var(--photo-pink) 80%,#f6dede 100%)}
.title-box{position:absolute;left:0;top:450px;width:423px;height:125px;background:var(--paper);padding:22px 0 0 36px}
.cover-title{font-weight:500;font-size:41px;color:var(--red);letter-spacing:2.6px;line-height:1;white-space:nowrap}
.cover-subtitle{font-family:"Oswald",sans-serif;font-weight:500;font-size:26px;color:var(--maroon);margin:12px 0 0 6px;line-height:1}
.brand{position:absolute;display:flex;align-items:center;gap:10px}
.brand-dot{border-radius:50%;background:var(--red);flex:none}
.brand-name{font-weight:700;color:var(--ink);white-space:nowrap}
.cover .brand{left:38px;top:660px}
.cover .brand-dot{width:58px;height:58px}
.cover .brand-name{font-size:25px}
.cover-contact{position:absolute;left:39px;top:734px;font-size:14.5px;font-weight:500;letter-spacing:1.1px;white-space:nowrap}
.cover .band{top:773px;height:47px;font-size:14px;font-weight:500;letter-spacing:.6px;padding-bottom:16px}

/* contents */
.contents{left:712px;top:42px;width:388px;height:545px}
.rule{position:absolute;height:3px}
.rule.red{left:0;top:30px;width:80px;background:var(--red)}
.rule.dark{left:168px;top:30px;width:178px;background:var(--maroon)}
.page-no{position:absolute;left:355px;top:26px;font-size:12px;font-weight:600}
.toc-title{position:absolute;left:26px;top:65px;font-family:"Noto Serif",serif;font-weight:400;font-size:15px;color:var(--red)}
.toc{position:absolute;left:28px;width:338px;list-style:none}
.toc li{height:22.3px;display:flex;align-items:center;font-family:"Noto Serif",serif;font-size:8px}
.toc .leader{flex:1;border-bottom:1px dotted #888;margin:0 2px 0 3px;height:1px;align-self:center;margin-top:4px}
.toc .num{width:52px;height:16px;text-align:right;padding-right:8px;line-height:16px;background:linear-gradient(90deg,#fff,#fbe1e4)}
.toc li:nth-child(odd) .num{background:linear-gradient(90deg,#fff,var(--red-soft))}
.toc.first{top:104px}
.toc.second{top:271px}
.contents .band{top:513px;height:32px;font-size:8px;font-weight:600;gap:8px;padding-bottom:12px}
.contents .band::before,.contents .band::after{content:"";width:70px;height:1px;background:#fff}

/* back */
.back{left:712px;top:613px;width:388px;height:545px}
.back .brand{left:26px;top:36px;gap:8px}
.back .brand-dot{width:38px;height:38px}
.back .brand-name{font-size:17px}
.back-rule{position:absolute;left:25px;top:87px;width:335px;height:1px;background:var(--red-soft)}
.statement{position:absolute;left:26px;top:100px;font-size:20px;font-weight:500;color:var(--red);letter-spacing:1.2px;line-height:29px}
.back-contact{position:absolute;left:22px;top:453px;font-size:10px;font-weight:500;line-height:16.5px;letter-spacing:.3px}
.back-address{position:absolute;left:181px;top:470px;border-left:1px solid var(--red);padding-left:8px;font-size:10px;font-weight:500;line-height:16.5px;letter-spacing:.3px}
.back .band{top:512px;height:33px}
</style>
</head>
<body>

<section class="page cover">
  <div class="cover-photo" role="img" aria-label="Photo of a smiling businesswoman on the phone at a laptop in front of a green plant wall, with a pink tint"></div>
  <div class="title-box">
    <h1 class="cover-title">YOUR TITLE HERE</h1>
    <p class="cover-subtitle">YOUR SUB TITLE HERE</p>
  </div>
  <div class="brand"><span class="brand-dot"></span><span class="brand-name">BRIM VANTAGE PARTNERS</span></div>
  <p class="cover-contact">1-555-014270 | mara@brimvantage.com | www.brimvantage.com</p>
  <footer class="band">Dummy City, Dummy Country, Land</footer>
</section>

<section class="page contents">
  <span class="rule red"></span><span class="rule dark"></span>
  <span class="page-no">02</span>
  <h2 class="toc-title">1. Table Of Contents</h2>
  <ol class="toc first">
    <li>Lorem Ipsum<span class="leader"></span><span class="num">1</span></li>
    <li>Lorem Ipsum<span class="leader"></span><span class="num">3</span></li>
    <li>Lorem Ipsum<span class="leader"></span><span class="num">3</span></li>
    <li>Lorem Ipsum<span class="leader"></span><span class="num">3</span></li>
    <li>Lorem Ipsum<span class="leader"></span><span class="num">4</span></li>
    <li>Lorem Ipsum<span class="leader"></span><span class="num">4</span></li>
    <li>Lorem Ipsum<span class="leader"></span><span class="num">4</span></li>
  </ol>
  <ol class="toc second">
    <li>Lorem Ipsum<span class="leader"></span><span class="num">1</span></li>
    <li>Lorem Ipsum<span class="leader"></span><span class="num">3</span></li>
    <li>Lorem Ipsum<span class="leader"></span><span class="num">3</span></li>
    <li>Lorem Ipsum<span class="leader"></span><span class="num">3</span></li>
    <li>Lorem Ipsum<span class="leader"></span><span class="num">4</span></li>
    <li>Lorem Ipsum<span class="leader"></span><span class="num">4</span></li>
    <li>Lorem Ipsum<span class="leader"></span><span class="num">4</span></li>
  </ol>
  <footer class="band">www.brimvantage.com</footer>
</section>

<section class="page back">
  <div class="brand"><span class="brand-dot"></span><span class="brand-name">BRIM VANTAGE PARTNERS</span></div>
  <span class="back-rule"></span>
  <p class="statement">BRIM<br>VANTAGE<br>RETAIL<br>PARTNERS</p>
  <p class="back-contact">1-555-014270<br>www.brimvantage.com<br>mara@brimvantage.com</p>
  <p class="back-address">Dummy City<br>Dummy Country, Land</p>
  <footer class="band"></footer>
</section>

</body>
</html>
```